Allied Health business card / Logo update.

Update/revitalise our logo and business cards. The logo needs to be suitable not only for business cards but stationary, website and clothing as well.

We have had the same hand logo for 16 years and have a strong brand name with this. One idea, however, was to base the idea around the similarities between the spine and bamboo. I will attach some images.

We are uncertain with colour. Initially, we thought earthy greens and greys/charcoal. However, we would also consider blue/charcoal combination.

I have attached our existing logo and this is our website. http://www.harbourleafspinal.com.au

Target Market(s)

General public
This is the only card

Industry/Entity Type

Health Care

Contact Information for Business Card

Harbourleaf Chiropractic Centre
27 Willowmere Road (Cnr Banfield St and Willowmere Rd) Lindale Bay
4/58 Thornbury St Ferndown
phone: 02 6571 4826
email: info@harbourleafspinal.com.au
web: harbourleafspinal.com.au

Marcus P. Helton
Cert. Rehab Therapist
Chiropractor
BSc(Hlth)., MChiroSc(Pr)., MClinRehab(Neuro)
MCRA, MSPN, VRDA

Font styles to use
Serif
Sans Serif

Colors
acd037
85acd3
5c5c5c

Requirements
Must have
• Company name, Professional name with qualifications
• Contact details.

```html
<!DOCTYPE html>
<html lang="en">
<head>
<meta charset="utf-8">
<title>Harbourleaf Chiropractic Centre – Business Card</title>
<link href="https://fonts.googleapis.com/css2?family=Cinzel:wght@500&family=Open+Sans:wght@400;600;700&display=swap" rel="stylesheet">
<style>
  :root{
    --bg:#3a3838;
    --card:#ffffff;
    --green-dark:#3f5a34;
    --green-mid:#5a7a45;
    --green-light:#7aa35f;
    --green-text:#4f8a2a;
    --grey:#5c5c5c;
    --text:#3d3d3d;
  }
  *{margin:0;padding:0;box-sizing:border-box}
  html,body{width:1200px;height:1200px;overflow:hidden}
  body{background:var(--bg);position:relative;font-family:"Open Sans",Arial,sans-serif;color:var(--text)}
  .card{position:absolute;width:660px;height:370px;background:var(--card);box-shadow:0 10px 30px rgba(0,0,0,.45);overflow:hidden}
  .card-front{left:110px;top:170px;display:flex;align-items:center;justify-content:center}
  .brand{display:flex;align-items:center;gap:22px}
  .brand-mark{width:88px;height:88px;background:var(--grey)}
  .brand-name{font-family:"Open Sans",Arial,sans-serif;font-weight:700;font-size:30px;line-height:1.08;color:var(--green-light)}
  .card-back{left:430px;top:640px;display:flex}
  .bamboo-art{width:240px;height:100%;flex:none;background:linear-gradient(90deg,var(--green-mid) 0%,var(--green-dark) 35%,#6f6f6f 50%,var(--green-dark) 65%,var(--green-mid) 100%)}
  .accent-band{width:36px;height:100%;flex:none;background:var(--green-light);margin-left:6px}
  .details{flex:1;padding:38px 26px 20px 0;text-align:right;font-size:11.5px;line-height:1.5;white-space:nowrap}
  .person-name{font-family:"Cinzel",Georgia,serif;font-weight:500;font-size:25px;color:var(--green-text);line-height:1.2;margin-bottom:4px}
  .company{font-weight:700;color:var(--green-text);margin-top:16px}
  .contact{display:flex;justify-content:flex-end;align-items:center;gap:6px;height:18px}
  .icon{width:14px;height:14px;flex:none}
</style>
</head>
<body>
  <section class="card card-front" aria-label="Card front">
    <div class="brand">
      <div class="brand-mark"></div>
      <div class="brand-name">Harbourleaf<br>Chiropractic<br>Centre</div>
    </div>
  </section>

  <section class="card card-back" aria-label="Card back">
    <div class="bamboo-art" role="img" aria-label="Illustration of green and grey bamboo stalks resembling a spine"></div>
    <div class="accent-band"></div>
    <div class="details">
      <p class="person-name">Marcus P. Helton</p>
      <p>Cert. Rehab Therapist</p>
      <p>Chiropractor</p>
      <p>BSc(Hlth)., MChiroSc(Pr)., MClinRehab(Neuro)</p>
      <p>MCRA, MSPN, VRDA</p>
      <p class="company">Harbourleaf Chiropractic Centre</p>
      <p>27 Willowmere Road (Cnr Banfield St and Willowmere Rd)</p>
      <p>Lindale Bay</p>
      <p>4/58 Thornbury St Ferndown</p>
      <p class="contact">02 6571 4826
        <svg class="icon" viewBox="0 0 16 16" aria-hidden="true"><circle cx="8" cy="8" r="8" fill="#4f8a2a"/><path d="M5 4.5l1.6-.4 1 2-1 .8a5 5 0 0 0 2.5 2.5l.8-1 2 1-.4 1.6c-3.5.2-6.6-2.9-6.5-6.5z" fill="#fff"/></svg>
      </p>
      <p class="contact">info@harbourleafspinal.com.au
        <svg class="icon" viewBox="0 0 16 16" aria-hidden="true"><circle cx="8" cy="8" r="8" fill="#4f8a2a"/><rect x="4" y="5" width="8" height="6" fill="#fff"/><path d="M4 5l4 3.3L12 5" stroke="#4f8a2a" stroke-width="1" fill="none"/></svg>
      </p>
      <p class="contact">harbourleafspinal.com.au
        <svg class="icon" viewBox="0 0 16 16" aria-hidden="true"><circle cx="8" cy="8" r="8" fill="#4f8a2a"/><circle cx="8" cy="8" r="4.5" stroke="#fff" fill="none"/><path d="M3.5 8h9M8 3.5c-2 2.5-2 6.5 0 9M8 3.5c2 2.5 2 6.5 0 9" stroke="#fff" stroke-width=".8" fill="none"/></svg>
      </p>
    </div>
  </section>
</body>
</html>
```